Travel Business Card

Hello. I am an award-winning travel advisor in Sydney, Australia seeking new business cards reflecting a unique style. Words to describe the design I'm seeking - Contemporary, Artsy, Vibrant, Soulful, Journey.

I loved this'Absolut' design and have created a few concepts to guide you for the back of the bus card. Feel free to use your own imagination...
maybe use elements of a Venetian mask or City (Icon), Cruise Ship, Sunshine, Beach/ Beach Hut, Buddha (Spiritual), Lotus or Palm Tree (Nature), Magic Carpet (Middle East), Whale or Waves, or enhance the pencil sketch I did...

Remember. The design should look high-end and fashionable.

Looking forward to hearing from you.
My email is miriam@plenvoritrips.example.

Many thanks.

```html
<!DOCTYPE html>
<html lang="en">
<head>
<meta charset="utf-8">
<title>Miriam Castell – Business Card</title>
<link rel="stylesheet" href="https://fonts.googleapis.com/css2?family=Cinzel:wght@400&family=Arimo:wght@400&display=swap">
<style>
  :root {
    --backdrop: #ece8e2;
    --card-white: #ffffff;
    --brand-red: #e8322d;
    --band-red: rgba(255, 92, 84, 0.85);
    --ink: #2b2b2b;
    --ink-soft: #5a5a5a;
  }
  * { margin: 0; padding: 0; box-sizing: border-box; }
  html, body {
    width: 1200px;
    height: 800px;
    overflow: hidden;
    background: var(--backdrop);
  }
  .stage {
    position: relative;
    width: 1200px;
    height: 800px;
  }
  .card {
    position: absolute;
    top: 247px;
    width: 500px;
    height: 306px;
    overflow: hidden;
    box-shadow: 0 6px 18px rgba(0, 0, 0, 0.12);
  }

  /* Back: illustrated red side */
  .card-back { left: 70px; }
  .card-back .artwork {
    position: absolute;
    inset: 0;
    width: 100%;
    height: 100%;
  }
  .card-back .web-band {
    position: absolute;
    left: 0;
    right: 0;
    top: 128px;
    height: 44px;
    background: var(--band-red);
    display: flex;
    align-items: center;
    padding-left: 70px;
  }
  .card-back .web-address {
    font-family: 'Arimo', Arial, sans-serif;
    font-size: 22px;
    color: var(--card-white);
    letter-spacing: 0.2px;
  }

  /* Front: white information side */
  .card-front {
    left: 630px;
    background: var(--card-white);
    font-family: 'Arimo', Arial, sans-serif;
    color: var(--ink);
  }
  .card-front .name {
    position: absolute;
    left: 96px;
    top: 42px;
    font-family: 'Cinzel', 'Times New Roman', serif;
    font-size: 30px;
    font-weight: 400;
    color: var(--brand-red);
    letter-spacing: 1px;
    white-space: nowrap;
  }
  .card-front .role {
    position: absolute;
    left: 150px;
    top: 86px;
    font-size: 13px;
    color: var(--ink);
  }
  .card-front .registration {
    position: absolute;
    left: 28px;
    top: 134px;
    font-size: 9.5px;
    line-height: 13px;
    color: var(--ink);
  }
  .card-front .contact {
    position: absolute;
    left: 262px;
    top: 128px;
    font-size: 13.5px;
    line-height: 17px;
    font-style: normal;
    color: var(--ink);
    white-space: nowrap;
  }
  .card-front .credentials {
    position: absolute;
    left: 262px;
    top: 226px;
    font-size: 9.5px;
    line-height: 12.5px;
    color: var(--ink-soft);
    white-space: nowrap;
  }
</style>
</head>
<body>
<main class="stage">

  <section class="card card-back">
    <svg class="artwork" viewBox="0 0 500 306" role="img" aria-label="Hand-drawn black ink travel illustration on red: palms, flowers, snowflakes, city skyline and a masked figure">
      <defs>
        <radialGradient id="artwork-tone" cx="50%" cy="50%" r="75%">
          <stop offset="0%" stop-color="#e8322d"/>
          <stop offset="100%" stop-color="#8e1816"/>
        </radialGradient>
      </defs>
      <rect width="500" height="306" fill="url(#artwork-tone)"/>
    </svg>
    <div class="web-band">
      <span class="web-address">www.MiriamCastell.example</span>
    </div>
  </section>

  <section class="card card-front">
    <h1 class="name">Miriam Castell</h1>
    <p class="role">Travel Advisor</p>

    <p class="registration">
      LIC No. 3TB55021<br>
      ABN. 12 345 678 901
    </p>

    <address class="contact">
      M.0400 555 218<br>
      F. 02 5550 1427<br>
      E.travel@miriamcastell.example<br>
      A. PO Box 4410<br>
      Tallowbrook, NSW 2999
    </address>

    <p class="credentials">
      Over 16 years experience<br>
      Leisure &amp; Corporate<br>
      Australian Cruise Consultant of the year<br>
      Southern Seas Cruise Guild 2008
    </p>
  </section>

</main>
</body>
</html>
```